We are wanting a designer to design an ebook on Residential Property in Australia. This ebook is a quarterly report and covers 5 major capital cities in Australia. This is the first quarterly report for the year - another 3 are needed to be created. If you are chosen as our designer please expect ongoing work which is well rewarded.

To begin with:

We will only need you to design a few pages so we can see your style. Then if you are chosen we will get you to do the whole thing.

Can you please design the title page, page 5 and the Adelaide section(page 6 & 7) of the The Suburban Dwelling Forecast - Seasonal Capital Briefing - Q1 2014 document attached.

The ebook brief:

You will need to create 2 graphs to include in the ebook from the data I give to you for each capital city (one graph for houses and one graph for units).

We already have a style of ebook in mind from a previous ebook our in-office designer has created for our company. You will need to keep with the logo/style/colours/fonts etc. We are looking for a designer based in Australia.

Sources and content:

Below I have shared a dropbox folder with you. It contains the first ebook our designer has created for you to view the style,logo etc - YieldHaven-Property-ebook. The folder also contains the source files for the logo.

https://www.filecrate-share.com/sh/k4p2xq7vb9rm3d/BXQ581zt/

The Suburban Dwelling Forecast - Seasonal Capital Briefing - Q1 2014 document attached is the content we need made into the ebook.

Each page has been set out with the content needed for that page. Each capital city content spreads out over two pages with a graph on each. I have highlighted in red the data needed to create each of the graphs. The graph style must look like the Sector Horizon image in the shared dropbox folder.

You will also need to redesign the graph on page 5. You may do this how you like as long as it keeps in the style of the ebook. We will also need the source files on this ebook.

```html
<!DOCTYPE html>
<html lang="en">
<head>
<meta charset="utf-8">
<title>Adelaide – Seasonal Capital Briefing</title>
<link href="https://fonts.googleapis.com/css2?family=Source+Sans+3:wght@400;600;700&display=swap" rel="stylesheet">
<style>
:root{
  --red:#c11a2b;
  --red-dark:#9e1321;
  --blue:#1f6cab;
  --green:#1e9a4b;
  --purple:#7a3f98;
  --orange:#ef7a2c;
  --ink:#2b2b2b;
  --grid:#f0b9c0;
  --line:#1b3d7a;
}
*{margin:0;padding:0;box-sizing:border-box}
html,body{width:848px;height:1200px;overflow:hidden;background:#fff}
body{font-family:"Source Sans 3",Arial,sans-serif;color:var(--ink);position:relative}
.hero-band{position:absolute;left:0;top:50px;width:848px;height:335px;
  background:linear-gradient(135deg,var(--red) 0%,var(--red-dark) 55%,var(--red) 100%)}
.hero-photo{position:absolute;left:235px;top:85px;width:613px;height:257px;
  background:linear-gradient(180deg,#b9b4ae 0%,#d8d2c8 45%,#8f8a7e 75%,#c8c2b6 100%)}
.city-title{position:absolute;left:26px;top:98px;color:#fff;font-weight:700;font-size:40px;letter-spacing:.3px}
.intro{position:absolute;left:57px;top:440px;width:735px;font-size:14.5px;line-height:21px}
.intro p{margin-bottom:20px}
.outlook-title{position:absolute;left:88px;top:752px;color:var(--red);font-weight:700;font-size:29px;letter-spacing:.2px}
.outlook-sub{position:absolute;left:90px;top:787px;color:var(--blue);font-size:15px}
.outlook-box{position:absolute;left:88px;top:812px;width:599px;height:264px;border:1.5px solid var(--red)}
.stats{display:grid;grid-template-columns:214px 185px 200px;grid-template-rows:50px 50px}
.stat{display:flex;align-items:center;border-right:1px solid #e6a7ae;border-bottom:1px solid #e6a7ae;padding-left:14px}
.stat:nth-child(3n){border-right:none}
.stat svg{width:22px;height:22px;flex:none}
.stat-label{width:62px;text-align:right;font-weight:700;font-size:10.5px;line-height:11px;color:var(--red);margin:0 9px 0 0;text-transform:uppercase}
.stat-value{font-size:24px;color:var(--blue)}
.lbl-green{color:var(--green)}.lbl-purple{color:var(--purple)}.lbl-orange{color:var(--orange)}.lbl-ink{color:var(--ink)}
.chart{position:absolute;left:0;top:0}
.brand{position:absolute;left:712px;top:1128px;display:flex;align-items:center;gap:8px;color:var(--red);font-weight:700;font-size:22px}
.brand span.mark{width:16px;height:16px;background:var(--red)}
</style>
</head>
<body>
<div class="hero-band"></div>
<div class="hero-photo" role="img" aria-label="Photo of a modern single-storey home with a white garage door and landscaped garden"></div>
<h1 class="city-title">Adelaide</h1>

<div class="intro">
  <p>The latest figures also indicate that more buyers are entering the metropolitan Adelaide market.</p>
  <p>SAPRI report that during the December 2013 quarter 4,314 houses were settled across metropolitan Adelaide. This compares well against the 3,786 properties that were settled in the same area 12 months prior.</p>
  <p>Across the entire state, 714 more properties were settled than in the same period last year. Over the entire year, there were almost 2,000 more settled sales in South Australia than in 2012.</p>
  <p>SAPRI also reports that over the past 12 months, Adelaide’s stand out growth suburbs were Glenelg North at 48.63%, Fullarton at 27.27% and Noarlunga Downs at 27.14%. Other big movers included Port Noarlunga and Brighton.</p>
</div>

<h2 class="outlook-title">2014 SECTOR HORIZON - UNITS</h2>
<p class="outlook-sub">Median values of Adelaide for the current quarter.</p>

<div class="outlook-box">
  <div class="stats">
    <div class="stat">
      <svg viewBox="0 0 22 22"><circle cx="11" cy="11" r="10" fill="var(--red)"/><text x="11" y="16" text-anchor="middle" font-size="14" font-weight="700" fill="#fff" font-family="Arial">$</text></svg>
      <div class="stat-label">Unit<br>Value</div><div class="stat-value">$305,000</div>
    </div>
    <div class="stat">
      <svg viewBox="0 0 22 22"><circle cx="11" cy="8" r="7" fill="var(--green)"/><rect x="9.5" y="12" width="3" height="9" fill="var(--green)"/></svg>
      <div class="stat-label lbl-green">Capital<br>Growth</div><div class="stat-value">1.52%</div>
    </div>
    <div class="stat">
      <svg viewBox="0 0 22 22" fill="var(--purple)"><rect x="2" y="15" width="3" height="5"/><rect x="7" y="11" width="3" height="9"/><rect x="12" y="7" width="3" height="13"/><rect x="17" y="3" width="3" height="17"/></svg>
      <div class="stat-label lbl-purple">Rental<br>Yield</div><div class="stat-value">5.14%</div>
    </div>
    <div class="stat">
      <svg viewBox="0 0 22 22" fill="var(--ink)"><path d="M11 2 1 11h3v9h5v-6h4v6h5v-9h3z"/></svg>
      <div class="stat-label lbl-ink">Unit<br>Sales</div><div class="stat-value">1,277</div>
    </div>
    <div class="stat">
      <svg viewBox="0 0 22 22"><rect x="2" y="4" width="18" height="16" rx="2" fill="var(--orange)"/><rect x="4" y="9" width="14" height="9" fill="#fff"/><g fill="var(--orange)"><rect x="5" y="10" width="3" height="3"/><rect x="10" y="10" width="3" height="3"/><rect x="15" y="10" width="2" height="3"/><rect x="5" y="14" width="3" height="3"/><rect x="10" y="14" width="3" height="3"/></g></svg>
      <div class="stat-label lbl-orange">Weekly<br>Rent</div><div class="stat-value">$300</div>
    </div>
    <div class="stat">
      <svg viewBox="0 0 22 22" fill="none" stroke="var(--ink)" stroke-width="2.2"><path d="M4 10V7h13"/><path d="M14 4l3 3-3 3"/><path d="M18 12v3H5"/><path d="M8 18l-3-3 3-3"/></svg>
      <div class="stat-label lbl-ink">Total<br>Return</div><div class="stat-value">0.31%</div>
    </div>
  </div>
</div>

<svg class="chart" width="848" height="1200" viewBox="0 0 848 1200" aria-label="Line chart of Adelaide unit median values, December 2003 to December 2013">
  <text x="654" y="929" text-anchor="end" font-size="10" fill="#777" font-family="Source Sans 3, Arial, sans-serif">Median Value - Adelaide Units</text>
  <g stroke="var(--grid)" stroke-width="1">
    <line x1="158" y1="950" x2="655" y2="950"/><line x1="158" y1="976" x2="655" y2="976"/><line x1="158" y1="1002" x2="655" y2="1002"/><line x1="158" y1="1028" x2="655" y2="1028"/><line x1="158" y1="1054" x2="655" y2="1054"/>
    <line x1="158" y1="950" x2="158" y2="1054"/><line x1="182.9" y1="950" x2="182.9" y2="1054"/><line x1="207.7" y1="950" x2="207.7" y2="1054"/><line x1="232.6" y1="950" x2="232.6" y2="1054"/><line x1="257.4" y1="950" x2="257.4" y2="1054"/><line x1="282.3" y1="950" x2="282.3" y2="1054"/><line x1="307.1" y1="950" x2="307.1" y2="1054"/><line x1="332" y1="950" x2="332" y2="1054"/><line x1="356.8" y1="950" x2="356.8" y2="1054"/><line x1="381.7" y1="950" x2="381.7" y2="1054"/><line x1="406.5" y1="950" x2="406.5" y2="1054"/><line x1="431.4" y1="950" x2="431.4" y2="1054"/><line x1="456.2" y1="950" x2="456.2" y2="1054"/><line x1="481.1" y1="950" x2="481.1" y2="1054"/><line x1="505.9" y1="950" x2="505.9" y2="1054"/><line x1="530.8" y1="950" x2="530.8" y2="1054"/><line x1="555.6" y1="950" x2="555.6" y2="1054"/><line x1="580.5" y1="950" x2="580.5" y2="1054"/><line x1="605.3" y1="950" x2="605.3" y2="1054"/><line x1="630.2" y1="950" x2="630.2" y2="1054"/><line x1="655" y1="950" x2="655" y2="1054"/>
  </g>
  <g font-size="10" fill="#444" font-family="Source Sans 3, Arial, sans-serif" text-anchor="end">
    <text x="148" y="953">$350,000</text><text x="148" y="979">$300,000</text><text x="148" y="1005">$250,000</text><text x="148" y="1031">$200,000</text><text x="148" y="1057">$150,000</text>
  </g>
  <polyline fill="none" stroke="var(--line)" stroke-width="1.6" points="158,1038.4 182.9,1032.2 207.7,1030.6 232.6,1025.4 257.4,1022.8 282.3,1016.6 307.1,1014.5 332,1004.6 356.8,992.6 381.7,976 406.5,977 431.4,973.4 456.2,971.8 481.1,966.6 505.9,964.6 530.8,963 555.6,964.6 580.5,970.8 605.3,971.8 630.2,973.9 655,972.4"/>
  <g fill="#fff" stroke="var(--blue)" stroke-width="2">
    <circle cx="158" cy="1038.4" r="3"/><circle cx="182.9" cy="1032.2" r="3"/><circle cx="207.7" cy="1030.6" r="3"/><circle cx="232.6" cy="1025.4" r="3"/><circle cx="257.4" cy="1022.8" r="3"/><circle cx="282.3" cy="1016.6" r="3"/><circle cx="307.1" cy="1014.5" r="3"/><circle cx="332" cy="1004.6" r="3"/><circle cx="356.8" cy="992.6" r="3"/><circle cx="381.7" cy="976" r="3"/><circle cx="406.5" cy="977" r="3"/><circle cx="431.4" cy="973.4" r="3"/><circle cx="456.2" cy="971.8" r="3"/><circle cx="481.1" cy="966.6" r="3"/><circle cx="505.9" cy="964.6" r="3"/><circle cx="530.8" cy="963" r="3"/><circle cx="555.6" cy="964.6" r="3"/><circle cx="580.5" cy="970.8" r="3"/><circle cx="605.3" cy="971.8" r="3"/><circle cx="630.2" cy="973.9" r="3"/>
  </g>
  <circle cx="655" cy="972.4" r="3.5" fill="#fff" stroke="var(--red)" stroke-width="2"/>
  <g font-size="9.5" fill="#444" font-family="Source Sans 3, Arial, sans-serif" text-anchor="middle">
    <text x="158" y="1087">DEC</text><text x="158" y="1099">2003</text>
    <text x="182.9" y="1087">JUN</text><text x="182.9" y="1099">2004</text>
    <text x="207.7" y="1087">DEC</text><text x="207.7" y="1099">2004</text>
    <text x="232.6" y="1087">JUN</text><text x="232.6" y="1099">2005</text>
    <text x="257.4" y="1087">DEC</text><text x="257.4" y="1099">2005</text>
    <text x="282.3" y="1087">JUN</text><text x="282.3" y="1099">2006</text>
    <text x="307.1" y="1087">DEC</text><text x="307.1" y="1099">2006</text>
    <text x="332" y="1087">JUN</text><text x="332" y="1099">2007</text>
    <text x="356.8" y="1087">DEC</text><text x="356.8" y="1099">2007</text>
    <text x="381.7" y="1087">JUN</text><text x="381.7" y="1099">2008</text>
    <text x="406.5" y="1087">DEC</text><text x="406.5" y="1099">2008</text>
    <text x="431.4" y="1087">JUN</text><text x="431.4" y="1099">2009</text>
    <text x="456.2" y="1087">DEC</text><text x="456.2" y="1099">2009</text>
    <text x="481.1" y="1087">JUN</text><text x="481.1" y="1099">2010</text>
    <text x="505.9" y="1087">DEC</text><text x="505.9" y="1099">2010</text>
    <text x="530.8" y="1087">JUN</text><text x="530.8" y="1099">2011</text>
    <text x="555.6" y="1087">DEC</text><text x="555.6" y="1099">2011</text>
    <text x="580.5" y="1087">JUN</text><text x="580.5" y="1099">2012</text>
    <text x="605.3" y="1087">DEC</text><text x="605.3" y="1099">2012</text>
    <text x="630.2" y="1087">JUN</text><text x="630.2" y="1099">2013</text>
    <text x="655" y="1087">DEC</text><text x="655" y="1099">2013</text>
  </g>
</svg>

<div class="brand"><span class="mark"></span>YieldHaven</div>
</body>
</html>
```